Acupuncture Medspa needs a business card design

I need a business card design that looks professional, has a spa-like quality and can offer a promo on the back. Initial promo is "First session free". The tagline of NeedleNook is: Refresh, Restore, Rejuvenate.

NeedleNook is a membership-based acupuncture medspa that offers acupuncture, cupping, and herbal therapies. Members choose between the "Refresh" membership which is for stress relief, or "Restore" which is for treating health conditions, and lastly "Rejuvenate" which is for natural facial enhancement.

Industry/Entity Type

Health And Wellness

Contact Information for Business Card

Coral Haskins, MAC, L.Ac.
612-555-0193
www.needlenook-example.com

Font styles to use
Serif
Sans Serif

Colors

Designer to choose colors to be used in the design.

Requirements
Must have
• The project must have NeedleNook logo, promo on the back, and contact information
Nice to have
• I would like to see the colors of the logo used.

```html
<!DOCTYPE html>
<html lang="en">
<head>
<meta charset="utf-8">
<title>NeedleNook Business Card</title>
<link href="https://fonts.googleapis.com/css2?family=Montserrat:wght@500;600;700;800&family=Quicksand:wght@500&display=swap" rel="stylesheet">
<style>
  :root {
    --teal: #138f8a;
    --teal-soft: #d5ecea;
    --paper: #ffffff;
    --backdrop: #e9eeee;
  }
  * { margin: 0; padding: 0; box-sizing: border-box; }
  html, body { width: 1200px; height: 800px; overflow: hidden; }
  body {
    background: var(--backdrop);
    display: flex;
    align-items: center;
    justify-content: center;
    gap: 40px;
    font-family: "Montserrat", sans-serif;
    color: var(--teal);
  }
  .card {
    width: 560px;
    height: 320px;
    background: var(--paper);
    border-radius: 24px;
    position: relative;
    overflow: hidden;
    box-shadow: 0 6px 20px rgba(0, 0, 0, 0.08);
  }

  /* Front */
  .card-front {
    display: flex;
    flex-direction: column;
    align-items: center;
    justify-content: center;
  }
  .brand {
    display: flex;
    align-items: center;
    gap: 12px;
  }
  .brand-dot {
    width: 22px;
    height: 22px;
    border-radius: 50%;
    background: var(--teal);
  }
  .brand-name {
    font-weight: 600;
    font-size: 50px;
    letter-spacing: 0.01em;
    line-height: 1;
  }
  .tagline {
    margin-top: 16px;
    font-weight: 800;
    font-size: 13.5px;
    letter-spacing: 0.22em;
    padding-bottom: 10px;
    border-bottom: 3px solid var(--teal);
  }
  .contact {
    margin-top: 20px;
    text-align: center;
    font-family: "Quicksand", sans-serif;
    font-weight: 500;
    font-size: 13px;
    letter-spacing: 0.1em;
    line-height: 23px;
  }

  /* Back */
  .card-back { display: flex; flex-direction: column; }
  .memberships {
    flex: 1;
    display: flex;
    justify-content: center;
    align-items: center;
    gap: 44px;
    padding-bottom: 6px;
  }
  .membership {
    display: flex;
    flex-direction: column;
    align-items: center;
    width: 110px;
  }
  .membership-icon {
    width: 58px;
    height: 60px;
    border-radius: 8px;
    background: var(--teal-soft);
  }
  .membership-label {
    margin-top: 16px;
    font-weight: 700;
    font-size: 13px;
    letter-spacing: 0.2em;
  }
  .promo-band {
    height: 82px;
    background: var(--teal);
    color: var(--paper);
    display: flex;
    align-items: center;
    justify-content: center;
    font-weight: 800;
    font-size: 22px;
    letter-spacing: 0.2em;
  }
</style>
</head>
<body>
  <section class="card card-front" aria-label="Business card front">
    <div class="brand">
      <span class="brand-name">NeedleNook</span>
      <span class="brand-dot"></span>
    </div>
    <p class="tagline">REFRESH, RESTORE, REJUVENATE</p>
    <div class="contact">
      <p>Coral Haskins, MAC, L.Ac.</p>
      <p>612-555-0193</p>
      <p>www.needlenook-example.com</p>
    </div>
  </section>

  <section class="card card-back" aria-label="Business card back">
    <div class="memberships">
      <div class="membership">
        <div class="membership-icon" role="img" aria-label="Line icon of two lit candles"></div>
        <p class="membership-label">REFRESH</p>
      </div>
      <div class="membership">
        <div class="membership-icon" role="img" aria-label="Line icon of bamboo stalks with leaves"></div>
        <p class="membership-label">RESTORE</p>
      </div>
      <div class="membership">
        <div class="membership-icon" role="img" aria-label="Line icon of a mortar and pestle"></div>
        <p class="membership-label">REJUVENATE</p>
      </div>
    </div>
    <div class="promo-band">FIRST SESSION FREE</div>
  </section>
</body>
</html>
```